Design eines Hausetiketts für traditionelles Weingut
Zielgruppe
Wir das Familienweingut Brosowski in Gimbsheim/Rheinhessen sind ein traditionelles Weingut das seine Reben selbst kultiviert und die Weine auch selbst ausbaut. Wir haben jeden Schritt in der Weinherstellung selbst in der Hand und vermarkten den Wein dann an unsere Privatkunden. Unsere Kundenstruktur sieht folgendermaßen aus: Wir haben 100% Privatkunden die unseren Wein konsumieren. Da jetzt die nächste Generation in den Weinbaubetrieb einsteigt und auch Ideen hat möchten wir ein Hausetikett einführen. Im Moment haben wir noch sehr viele unterschiedliche Etiketten und kein Hausetikett. Da die Verlagsetiketten immer seltener zu unseren Vorstellungen passen, möchten wir hier auf diesem Wege ein Hausetikett anfertigen lassen. Generell möchten wir unseren Außenauftritt komplett modernisieren. Sie können sich über die Vielfalt in unserem Betrieb unter www.weingut-brosowski-beispiel.de einen Überblick verschaffen. Langfristig gesehen wollen wir aber unsere Weinkarte verkleinern.
Aufgabenstellung
Wir haben uns vor ca. 1,5 Jahren hier auf dieser Website bereits ein Logo designen lassen. Es wäre schön wenn man das Logo bei den Entwürfen für die Etiketten berücksichtigen würde. Das wäre aber KEIN MUSS. Auch wäre es gut wenn man das ,,Wein' bei unserem Namen weglassen könnte.
Das Etikett sollte aus Vorder-und Rückenetikett bestehen und edel wirken. Vorne sollte die Rebsorte und die Geschmacksangabe stehen. Der Rest sollte auf das Rückenetikett.
Das Vorderetikett sollte ein richtiger Eyecatcher sein und im Supermarkt z.B. aus vielen anderen herausstechen. Das wäre ganz wichtig.
Man kann bei den Farben unterscheiden in 3 Konzepte.
Literwein als einsteiger Wein
Dann die Gutsweine und zum Schluss die Lagenweine. Alles Farblich oder im design etwas abgesetzt.

```html
<!DOCTYPE html>
<html lang="de">
<head>
<meta charset="utf-8">
<title>Brosowski – Hausetikett Vorder- und Rückseite</title>
<link rel="stylesheet" href="https://fonts.googleapis.com/css2?family=Cinzel:wght@400&family=Questrial&family=Nunito+Sans:wght@400;700&family=Arimo:ital@1&display=swap">
<style>
  :root {
    --bg: #e4e4e4;
    --paper: #ffffff;
    --ink: #111111;
    --night: #0b0b0b;
    --bronze: #b98b62;
    --wine-red: #ec1622;
    --accent-red: #e8141f;
    --label-grey: #8d8d8d;
    --cluster-light: #ececec;
    --cluster-dark: #3a2d22;
    --cluster-red: #f04a52;
  }
  * { margin: 0; padding: 0; box-sizing: border-box; }
  html, body { width: 1200px; height: 782px; overflow: hidden; }
  body { background: var(--bg); position: relative; font-family: "Questrial", sans-serif; }

  .front-label { position: absolute; overflow: hidden; }
  .front-label--liter { left: 248px; top: 339px; width: 126px; height: 222px; background: var(--paper); }
  .front-label--lage  { left: 424px; top: 322px; width: 142px; height: 257px; background: var(--night); }
  .front-label--guts  { left: 604px; top: 339px; width: 126px; height: 222px; background: var(--wine-red); }

  .front-label__name { position: absolute; left: 2px; top: 4px; width: 36px; height: 214px; }
  .front-label--lage .front-label__name { left: 2px; top: 4px; width: 40px; height: 250px; }
  .front-label__name text { font-family: "Cinzel", serif; font-weight: 400; }
  .front-label--liter .front-label__name text { fill: var(--ink); }
  .front-label--lage  .front-label__name text { fill: var(--bronze); }
  .front-label--guts  .front-label__name text { fill: var(--paper); }

  .front-label__cluster {
    position: absolute;
    border-radius: 50% 0 0 50% / 40% 0 0 60%;
  }
  .front-label--liter .front-label__cluster { left: 48px; top: 9px; width: 78px; height: 152px; background: var(--cluster-light); }
  .front-label--lage  .front-label__cluster { left: 53px; top: 13px; width: 89px; height: 178px; background: linear-gradient(160deg, #4a3a2b, var(--cluster-dark)); }
  .front-label--guts  .front-label__cluster { left: 49px; top: 9px; width: 77px; height: 152px; background: var(--cluster-red); }

  .front-label__info {
    position: absolute;
    left: 36px;
    bottom: 4px;
    font-family: "Cinzel", serif;
    font-size: 7px;
    line-height: 8px;
    letter-spacing: 0.03em;
  }
  .front-label--liter .front-label__info { color: var(--accent-red); }
  .front-label--lage  .front-label__info { left: 41px; color: var(--paper); font-size: 8.5px; line-height: 9px; }
  .front-label--guts  .front-label__info { color: var(--paper); }

  .back-heading {
    position: absolute;
    left: 859px;
    top: 189px;
    font-family: "Arimo", sans-serif;
    font-style: italic;
    font-size: 16px;
    color: var(--label-grey);
  }
  .back-label {
    position: absolute;
    left: 860px;
    top: 216px;
    width: 210px;
    height: 373px;
    background: var(--paper);
  }
  .back-label__mark {
    position: absolute;
    left: 50%;
    top: 24px;
    width: 20px;
    height: 20px;
    margin-left: -10px;
    border-radius: 50%;
    background: var(--accent-red);
  }
  .back-label__name {
    position: absolute;
    top: 56px;
    width: 100%;
    text-align: center;
    font-family: "Cinzel", serif;
    font-weight: 400;
    font-size: 26px;
    color: var(--ink);
  }
  .back-label__text {
    position: absolute;
    top: 123px;
    left: 28px;
    width: 154px;
    text-align: center;
    font-size: 13px;
    line-height: 16.5px;
    color: var(--ink);
  }
  .back-label__address {
    position: absolute;
    left: 5px;
    bottom: 6px;
    font-family: "Nunito Sans", sans-serif;
    font-size: 9.5px;
    line-height: 12px;
    color: var(--ink);
  }
  .back-label__address strong { font-weight: 700; }
  .back-label__volume {
    position: absolute;
    right: 7px;
    bottom: 6px;
    text-align: right;
    font-family: "Nunito Sans", sans-serif;
    font-size: 9.5px;
    line-height: 12px;
    color: var(--accent-red);
  }
</style>
</head>
<body>

  <section class="front-label front-label--liter">
    <svg class="front-label__name" viewBox="0 0 36 214">
      <text transform="translate(33 213) rotate(-90)" font-size="42" textLength="212" lengthAdjust="spacingAndGlyphs">BROSOWSKI</text>
    </svg>
    <div class="front-label__cluster" role="img" aria-label="Linienornament einer Traube in Schwarz"></div>
    <p class="front-label__info">2019<br>LITERWEIN<br>GESCHMACK</p>
  </section>

  <section class="front-label front-label--lage">
    <svg class="front-label__name" viewBox="0 0 40 250">
      <text transform="translate(37 249) rotate(-90)" font-size="47" textLength="247" lengthAdjust="spacingAndGlyphs">BROSOWSKI</text>
    </svg>
    <div class="front-label__cluster" role="img" aria-label="Linienornament einer Traube in Bronze"></div>
    <p class="front-label__info">2019<br>LAGENWEIN<br>GESCHMACK</p>
  </section>

  <section class="front-label front-label--guts">
    <svg class="front-label__name" viewBox="0 0 36 214">
      <text transform="translate(33 213) rotate(-90)" font-size="42" textLength="212" lengthAdjust="spacingAndGlyphs">BROSOWSKI</text>
    </svg>
    <div class="front-label__cluster" role="img" aria-label="Linienornament einer Traube in Weiß"></div>
    <p class="front-label__info">2019<br>GUTSWEIN<br>GESCHMACK</p>
  </section>

  <p class="back-heading">RÜCKSEITE:</p>
  <section class="back-label">
    <span class="back-label__mark"></span>
    <h1 class="back-label__name">BROSOWSKI</h1>
    <p class="back-label__text">Lorem ipsum dolor sit amet, consectetuer adipiscing elit, sed diam nonummy nibh euismod tincidunt ut laoreet dolore magna aliquam erat volutpat.</p>
    <p class="back-label__address"><strong>Weingut Brosowski</strong><br>Lindenweg 7<br>12345 Rebenfeld<br>Tel. 0 12 34 - 56 78</p>
    <p class="back-label__volume">℮ 750 ml<br>11,5% Vol.</p>
  </section>

</body>
</html>
```